Labels/logo for luxury bath products

I am developing a range of luxury bath foams - aimed at the top end of the luxury market. My company name is VEM (very basic website can be seen at www.vemarton.example).

I am looking for a label design for the front of the bottle, which should incorporate the VEM logo as per the website (file attached), but embedded within a more intricate label design. I provide a link to a picture of the bottle below.

The bath foam will come in four fragrances: Vetiver, Sandalwood, Jasmine and Neroli. The label should include the fragrance name. So the label must include the brand name 'VEM' and the name of the fragrance - e.g. Sandalwood Bath Foam, Neroli Bath Foam, etc.

The products are aimed at both the male and female market and so shouldn't be too feminine.

A brand to take inspiration from is Lune Bravière: http://www.lunebraviere.example/ - I like the labels that they use on their products, which is a gold embossed crest, which they use as the label for their products. I am not referring to their font, but to their label design - I like the embossed label, and am quite keen on metallics.

Conversely, I would like to add a contemporary edge to this design - I like the striping and contemporary fonts on this design: http://www.hadley-frost.example/images/fac83.jpg

My brand also harnesses the powers of natural flower ingredients, and so I am inspired by the products of Quenby - quenby.example. This labelling is more clinical and scientific.

Ideally I would like a label which combines these elements - i.e. a luxury label with a contemporary feel, that incorporate the scientific nature of the product.

The design needs to communicate high end luxury. The bottle is however apothecary style, and a nod to science and botany would be good. I would however like a bold approach to this design - it is a modern brand.

The bottle being used for the product can be seen at: http://www.tavel-vitro.example/en/product-groups/8-Apothecary-bottles - these are extremely expensive bottles and the label needs to reflect this quality. These bottles are traditional in design, but incorporate high end glassware technology to preserve the integrity of the natural ingredients. Therefore the product is a mix of old and new, and the label could also reflect this. The colour of the glass is very deep purple.

The front label does not need information such as weight/volume - it purely needs a label which will recognise it as the VEM brand, with the product name. I am looking for a high quality label, which is unique. I am happy to print embossed labels and to use foils on my labels.

Please do not be boring! I appreciate I have given a variety of influences, so summarise the requirements are a mix of:

a bold design
contemporary
luxury

The label must include NO slogans.

I am looking to build a relationship with a graphic designer for packaging and website design requirements so this will be the first of many projects.

Target Market(s)

Luxury end of market - clientele will like luxury and will pay for the highest quality ingredients in the product, but will also appreciate the botanical nature of the product.

Industry/Entity Type

Graphic Designer

Requirements
Must have
• Must include the company name, VEM, although this doesn't need to be particularly prominent. And the product name, e.g. Sandalwood.
Nice to have
• It should combine luxury, but with recognition of the science behind the product.
Should not have
• No slogans, minimal wording on the front label. No other wording other than company name and product name. No primary colours.

```html
<!DOCTYPE html>
<html lang="en">
<head>
<meta charset="utf-8">
<title>VEM Bath Foam Labels</title>
<link href="https://fonts.googleapis.com/css2?family=Oswald:wght@300;400&display=swap" rel="stylesheet">
<style>
  :root {
    --backdrop: #1c1c1f;
    --tab: #111111;
    --tab-text: #ffffff;
    --ink-dark: #2a2418;
    --ink-light: #ffffff;
    --gold-a: #8a6d1f;
    --gold-b: #e9d27a;
    --gold-c: #b8922e;
    --green-a: #0f8a3c;
    --green-b: #1fb154;
    --violet-a: #5a4596;
    --violet-b: #7a63b8;
    --silver-a: #8d8d8d;
    --silver-b: #f2f2f2;
    --silver-c: #b5b5b5;
  }
  html, body {
    margin: 0;
    padding: 0;
    overflow: hidden;
  }
  body {
    width: 1200px;
    height: 1018px;
    background: var(--backdrop);
    position: relative;
    font-family: "Oswald", "Arial Narrow", sans-serif;
  }
  .label {
    position: absolute;
    width: 460px;
    height: 345px;
  }
  .label-shape {
    position: absolute;
    inset: 0;
    width: 100%;
    height: 100%;
  }
  .brand-tab {
    position: absolute;
    left: 22px;
    top: -38px;
    width: 96px;
    height: 96px;
    background: var(--tab);
    display: flex;
    align-items: center;
    justify-content: center;
  }
  .brand-name {
    color: var(--tab-text);
    font-weight: 400;
    font-size: 34px;
    letter-spacing: 1px;
  }
  .fragrance {
    position: absolute;
    left: 0;
    right: 0;
    top: 96px;
    text-align: center;
    font-weight: 300;
    font-size: 74px;
    line-height: 1;
    margin: 0;
  }
  .product-type {
    position: absolute;
    left: 0;
    right: 0;
    top: 198px;
    text-align: center;
    font-weight: 300;
    font-size: 34px;
    margin: 0;
  }
  .label--metal .fragrance,
  .label--metal .product-type { color: var(--ink-dark); }
  .label--colour .fragrance,
  .label--colour .product-type { color: var(--ink-light); }

  .label--sandalwood { left: 110px; top: 120px; }
  .label--vetiver { left: 630px; top: 120px; }
  .label--neroli { left: 110px; top: 590px; }
  .label--jasmine { left: 630px; top: 590px; }
</style>
</head>
<body>
  <svg width="0" height="0" style="position:absolute">
    <defs>
      <linearGradient id="foil-gold" x1="0" y1="0" x2="1" y2="1">
        <stop offset="0" stop-color="var(--gold-a)"/>
        <stop offset="0.45" stop-color="var(--gold-b)"/>
        <stop offset="1" stop-color="var(--gold-c)"/>
      </linearGradient>
      <linearGradient id="ink-green" x1="0" y1="0" x2="1" y2="1">
        <stop offset="0" stop-color="var(--green-a)"/>
        <stop offset="1" stop-color="var(--green-b)"/>
      </linearGradient>
      <linearGradient id="ink-violet" x1="0" y1="0" x2="1" y2="1">
        <stop offset="0" stop-color="var(--violet-a)"/>
        <stop offset="1" stop-color="var(--violet-b)"/>
      </linearGradient>
      <linearGradient id="foil-silver" x1="0" y1="0" x2="1" y2="1">
        <stop offset="0" stop-color="var(--silver-a)"/>
        <stop offset="0.5" stop-color="var(--silver-b)"/>
        <stop offset="1" stop-color="var(--silver-c)"/>
      </linearGradient>
    </defs>
  </svg>

  <section class="label label--metal label--sandalwood">
    <svg class="label-shape" viewBox="0 0 200 150" preserveAspectRatio="none" aria-hidden="true">
      <path d="M10,8 Q100,0 190,6 Q200,70 186,140 Q100,150 30,146 Q4,140 6,80 Z" fill="url(#foil-gold)"/>
    </svg>
    <div class="brand-tab"><span class="brand-name">VEM</span></div>
    <h2 class="fragrance">Sandalwood</h2>
    <p class="product-type">Bath Foam</p>
  </section>

  <section class="label label--colour label--vetiver">
    <svg class="label-shape" viewBox="0 0 200 150" preserveAspectRatio="none" aria-hidden="true">
      <path d="M10,8 Q100,0 190,6 Q200,70 186,140 Q100,150 30,146 Q4,140 6,80 Z" fill="url(#ink-green)"/>
    </svg>
    <div class="brand-tab"><span class="brand-name">VEM</span></div>
    <h2 class="fragrance">Vetiver</h2>
    <p class="product-type">Bath Foam</p>
  </section>

  <section class="label label--colour label--neroli">
    <svg class="label-shape" viewBox="0 0 200 150" preserveAspectRatio="none" aria-hidden="true">
      <path d="M10,8 Q100,0 190,6 Q200,70 186,140 Q100,150 30,146 Q4,140 6,80 Z" fill="url(#ink-violet)"/>
    </svg>
    <div class="brand-tab"><span class="brand-name">VEM</span></div>
    <h2 class="fragrance">Neroli</h2>
    <p class="product-type">Bath Foam</p>
  </section>

  <section class="label label--metal label--jasmine">
    <svg class="label-shape" viewBox="0 0 200 150" preserveAspectRatio="none" aria-hidden="true">
      <path d="M10,8 Q100,0 190,6 Q200,70 186,140 Q100,150 30,146 Q4,140 6,80 Z" fill="url(#foil-silver)"/>
    </svg>
    <div class="brand-tab"><span class="brand-name">VEM</span></div>
    <h2 class="fragrance">Jasmine</h2>
    <p class="product-type">Bath Foam</p>
  </section>
</body>
</html>
```